Email Banner (LumenBriefs)

We require an email banner for our email promotions sent to prospect clients. The banner needs to contain the wording LumenBriefs and use the same colour scheme as the logos attached.

This is for B2B professional's so needs to look like a place you would come to read technology articles.

```html
<!DOCTYPE html>
<html lang="en">
<head>
<meta charset="utf-8">
<title>LumenBriefs Email Banner</title>
<link rel="stylesheet" href="https://fonts.googleapis.com/css2?family=Montserrat:wght@500;700&family=Poppins:wght@600&display=swap">
<style>
  :root {
    --page-bg: #c9c9c9;
    --banner-white: #ffffff;
    --navy: #031226;
    --ink: #0d1626;
    --green: #72bd55;
    --blue: #0a8fd2;
    --teal-soft: #bfeff2;
    --green-soft: #d4f4dc;
    --white: #ffffff;
  }
  * { margin: 0; padding: 0; box-sizing: border-box; }
  html, body {
    width: 1200px;
    height: 512px;
    overflow: hidden;
    background: var(--page-bg);
  }
  .banner {
    position: absolute;
    left: 0;
    top: 118px;
    width: 1200px;
    height: 276px;
    background: var(--banner-white);
    overflow: hidden;
  }
  .banner__header {
    position: relative;
    height: 171px;
    background: var(--banner-white);
  }
  .network-art {
    position: absolute;
    top: 0;
    height: 171px;
    width: 240px;
  }
  .network-art--left {
    left: 0;
    background: linear-gradient(90deg, var(--teal-soft) 0%, rgba(255,255,255,0) 100%);
  }
  .network-art--right {
    right: 0;
    background: linear-gradient(270deg, var(--teal-soft) 0%, var(--green-soft) 45%, rgba(255,255,255,0) 100%);
  }
  .brand {
    position: absolute;
    left: 200px;
    top: 34px;
    display: flex;
    align-items: center;
    gap: 22px;
  }
  .brand__mark {
    width: 22px;
    height: 22px;
    border-radius: 50%;
    background: var(--blue);
  }
  .brand__name {
    font-family: "Montserrat", sans-serif;
    font-weight: 500;
    font-size: 88px;
    line-height: 1;
    letter-spacing: -1px;
    color: var(--ink);
  }
  .banner__footer {
    position: relative;
    height: 105px;
    background: var(--navy);
  }
  .contact {
    position: absolute;
    top: 21px;
    height: 48px;
    display: flex;
    align-items: center;
    color: var(--white);
    font-family: "Poppins", sans-serif;
    font-weight: 600;
  }
  .contact--phone {
    left: 137px;
    width: 370px;
    padding-left: 50px;
    background: var(--green);
    clip-path: polygon(48px 0, 100% 0, calc(100% - 48px) 100%, 0 100%);
    font-size: 29px;
    letter-spacing: 0.5px;
  }
  .contact--web {
    left: 497px;
    width: 579px;
    padding-left: 90px;
    background: var(--blue);
    clip-path: polygon(48px 0, 100% 0, calc(100% - 48px) 100%, 0 100%);
    font-size: 27px;
    letter-spacing: 4px;
  }
  .contact__icon {
    width: 24px;
    height: 24px;
    margin-right: 14px;
    flex: none;
  }
  .contact--phone { z-index: 2; }
  .contact--web { left: 540px; padding-left: 48px; }
</style>
</head>
<body>
  <section class="banner">
    <header class="banner__header">
      <div class="network-art network-art--left" role="img" aria-label="Soft teal network of connected dots"></div>
      <div class="network-art network-art--right" role="img" aria-label="Soft green and teal network of connected dots"></div>
      <div class="brand">
        <span class="brand__mark"></span>
        <h1 class="brand__name">LumenBriefs.io</h1>
      </div>
    </header>
    <footer class="banner__footer">
      <div class="contact contact--phone">
        <svg class="contact__icon" viewBox="0 0 24 24" aria-hidden="true">
          <circle cx="12" cy="12" r="12" fill="#031226"/>
          <path d="M8.2 6.5c.4-.3 1-.3 1.3.1l1.3 1.8c.3.4.2.9-.1 1.2l-.8.7c.6 1.4 1.6 2.5 3 3.2l.7-.8c.3-.3.8-.4 1.2-.1l1.8 1.3c.4.3.5.9.1 1.3l-.9 1c-.6.6-1.5.8-2.3.5-3.1-1.2-5.4-3.6-6.5-6.7-.3-.8-.1-1.7.5-2.3z" fill="#72bd55"/>
        </svg>
        <span class="contact__text">555 0142 0199</span>
      </div>
      <div class="contact contact--web">
        <svg class="contact__icon" viewBox="0 0 24 24" aria-hidden="true">
          <circle cx="12" cy="12" r="11" fill="#031226"/>
          <g fill="none" stroke="#0a8fd2" stroke-width="1.4">
            <ellipse cx="12" cy="12" rx="4.5" ry="10"/>
            <line x1="12" y1="2" x2="12" y2="22"/>
            <line x1="2" y1="12" x2="22" y2="12"/>
            <line x1="4" y1="7" x2="20" y2="7"/>
            <line x1="4" y1="17" x2="20" y2="17"/>
          </g>
        </svg>
        <span class="contact__text">www.lumenbriefs.io</span>
      </div>
    </footer>
  </section>
</body>
</html>
```